Small Production Wine Needs a Wine Label Design

We need a wine bottle label design for a hand crafted Petite Sirah wine produced by two friends in the wine industry. The wine brand will be called, BT (the first initials of each of their last names, Bellamy Thorne). The petite sirah grapes are from the Bellamy vineyard in the Russian River Valley of Sonoma County, and Thorne is the winemaker. Bellamy is a third generation farmer in sonoma county and also raised cattle on the same ranch the grapes were grown. Thorne is an experienced Winemaker and helped increase the quality of wines from Lodi, CA at a small boutique winery. For the front label, we would like the BT to look like a cattle brand, the font to be color black. We would like to include somewhere on the label Bellamy Thorne, maybe underneath the cattle brand in smaller font. We also need to include the appellation on the label, Russian River Valley, and in smaller font Sonoma County. Also, the varietal of the wine is Petite Sirah and the vintage is 2013. We are aiming for a simple and relatively classy label, yet with a rustic touch. We would like the label to be rectangular and have an organic/linen look to it. Also the incorporation of a ridge or mountain range in the back ground or subtly in the label would be cool.

```html
<!DOCTYPE html>
<html lang="en">
<head>
<meta charset="utf-8">
<title>Bellamy Thorne Petite Sirah Labels</title>
<link href="https://fonts.googleapis.com/css2?family=Questrial&display=swap" rel="stylesheet">
<style>
  :root {
    --page: #ffffff;
    --linen: #efede9;
    --linen-edge: #e6e3de;
    --ink: #2a2a2a;
    --ink-soft: #555555;
    --black-label: #151515;
    --black-label-edge: #222222;
    --white-ink: #f2f2f2;
    --grey-ink: #9a9a9a;
    --red: #d0243a;
    --pink: #e0345a;
    --ridge-light: #d9d6d1;
  }
  * { margin: 0; padding: 0; box-sizing: border-box; }
  html, body { width: 1200px; height: 1188px; overflow: hidden; background: var(--page); }
  body { position: relative; font-family: "Questrial", sans-serif; color: var(--ink); }

  .label {
    position: absolute;
    background: linear-gradient(160deg, var(--linen), var(--linen-edge));
    text-align: center;
  }
  .label > * { position: absolute; left: 0; right: 0; margin: 0 auto; }
  .label--main { left: 163px; top: 567px; width: 232px; height: 281px; }
  .label--foil { left: 472px; top: 401px; width: 251px; height: 321px; }
  .label--classic { left: 472px; top: 745px; width: 251px; height: 321px; }
  .label--black {
    left: 838px; top: 540px; width: 224px; height: 315px;
    background: linear-gradient(160deg, var(--black-label-edge), var(--black-label));
    color: var(--white-ink);
  }

  .brand-mark { font-size: 42px; letter-spacing: 1px; line-height: 1; color: var(--ink); }
  .vintage { font-size: 10px; letter-spacing: 3px; line-height: 1; color: var(--ink-soft); }
  .ridge-art {
    height: 40px; width: 70%;
    background: linear-gradient(180deg, var(--ridge-light), transparent);
    border-radius: 40% 40% 0 0;
  }
  .winery-name { font-size: 17px; letter-spacing: 1px; font-weight: 400; line-height: 1.2; color: var(--ink); }
  .subtitle { font-size: 8.5px; letter-spacing: 2.5px; line-height: 1; color: var(--ink-soft); }
  .varietal { font-size: 11px; letter-spacing: 2px; line-height: 1; color: var(--ink); }
  .appellation { font-size: 7px; letter-spacing: 1px; color: var(--ink-soft); line-height: 1.3; }

  .label--foil .brand-mark { color: #8c9a98; }
  .label--foil .varietal { color: var(--pink); }

  .label--black .brand-mark { color: var(--red); font-size: 34px; }
  .label--black .vintage { color: var(--white-ink); }
  .label--black .ridge-art { background: linear-gradient(180deg, #4a4a4a, transparent); }
  .label--black .winery-name { color: var(--white-ink); font-size: 16px; }
  .label--black .subtitle { color: var(--grey-ink); }
  .label--black .varietal { color: var(--red); }
  .label--black .appellation { color: var(--grey-ink); }
</style>
</head>
<body>

  <section class="label label--main">
    <div class="brand-mark" style="top:18px">BT</div>
    <div class="vintage" style="top:68px">2013</div>
    <div class="ridge-art" role="img" aria-label="Line drawing of a mountain range" style="top:82px; width:86%"></div>
    <h1 class="winery-name" style="top:153px">BELLAMY THORNE</h1>
    <div class="subtitle" style="top:183px">RANCH WINE</div>
    <div class="varietal" style="top:210px">PETITE SIRAH</div>
    <div class="appellation" style="top:245px">RUSSIAN RIVER VALLEY<br>SONOMA COUNTRY</div>
  </section>

  <section class="label label--foil">
    <div class="vintage" style="top:22px">2013</div>
    <div class="ridge-art" role="img" aria-label="Line drawing of a mountain range" style="top:38px; width:80%"></div>
    <div class="brand-mark" style="top:86px; font-size:48px">BT</div>
    <div class="subtitle" style="top:171px">RANCH WINE</div>
    <h2 class="winery-name" style="top:193px">BELLAMY THORNE</h2>
    <div class="varietal" style="top:240px">PETITE SIRAH</div>
    <div class="appellation" style="top:279px">RUSSIAN RIVER VALLEY<br>SONOMA COUNTRY</div>
  </section>

  <section class="label label--classic">
    <div class="brand-mark" style="top:32px; font-size:48px">BT</div>
    <div class="vintage" style="top:102px">2013</div>
    <div class="ridge-art" role="img" aria-label="Line drawing of a mountain range" style="top:116px; width:80%"></div>
    <h2 class="winery-name" style="top:192px">BELLAMY THORNE</h2>
    <div class="subtitle" style="top:223px">RANCH WINE</div>
    <div class="varietal" style="top:256px">PETITE SIRAH</div>
    <div class="appellation" style="top:293px">RUSSIAN RIVER VALLEY<br>SONOMA COUNTRY</div>
  </section>

  <section class="label label--black">
    <div class="brand-mark" style="top:62px">BT</div>
    <div class="vintage" style="top:100px">2013</div>
    <div class="ridge-art" role="img" aria-label="Line drawing of a mountain range" style="top:122px; width:76%"></div>
    <h2 class="winery-name" style="top:173px">BELLAMY THORNE</h2>
    <div class="subtitle" style="top:203px">RANCH WINE</div>
    <div class="varietal" style="top:256px">PETITE SIRAH</div>
    <div class="appellation" style="top:274px">RUSSIAN RIVER VALLEY<br>SONOMA COUNTRY</div>
  </section>

</body>
</html>
```